Tintmarble app graphic design
Graphics and layout of our Tintmarble app
Project: Tintmarble app graphic design
Tintmarble app graphic design - Photography
Creative Brief
Photography
www.brightvole.net
This software allows the user to easily change a color photo to a black and white photo with colored areas. No photo editing experience necessary. This project is the Tintmarble app version of the software. We need a design layout/template of the app. The canvas area will need to stay the same size, it is what it is, so use that as a starting point. The controls can be moved a bit, but only if necessary. Everything else you can design how you see fit, including the graphics behind the controls. Obviously, the goal is to make this app look appealing and friendly so users will want to use it. I will explain the different sections of the app in the additional comments section.
Like the black and white and use of different bold colors / gradients.
Colorful
Soft
left side
http://apps.tintmarble.example/huepickerbench/
The link to the live app is provided in the referred websites section. Also, see our main website www.brightvole.net for reference. Starting with the canvas area (diagonal lines) and build from there. The canvas is 640x530. We will provide the logo to incorporate above the canvas and control section. The tagline is "Easily change your photos from Color... to Black & White AND Color!" Below the app we need the following sections: A chart comparing features / benefits of this version and the full version. Has a click here to save $10 off full version An area to advertise the website PrintsOnSlate.example with a click here to save 20% off all products. An area to place a banner ad of general size that will rotate different banners. An area to pitch the photo contest that users can enter when they edit their photos in Hue Picker Bench Lite.
lumtavo lumtavo
karvel904: we like #11 and #12. The red headers and buttons are great. Instead of using that red in every location could you incorporate a couple of other colors? For instance, one is red, one blue, one green or yellow. (keeping the same bold values)
karvel904 - great design! Use less pink and a white background. Recommend using different bold colors.
Also, we prefer white background. Please see this link: http://www.layoutorca.example/shopkit-themes/58172.html The bold colors on the dark grey area really stand out. If you could incorporate this type of design it would be best.
Hello everyone. Thanks for the designs already submitted. I just uploaded an image, example.jpg, that shows how to layout the design. The green areas are the areas to concentrate on.
delmoraxx delmoraxx
Sir your brief do not have a proper idea...too many constants adds..give me the proper layout ..Thanks.
PlumtreeArtwork PlumtreeArtwork
can you give me the proper layout of app in what ever format so that i can get idea proper alignment of gui kit in app
Sir, I am working in on that.thanks.
SiteAdmin SiteAdmin
Attention Designers, Our policy for stock photos has changed and is effective immediately. QuillVantor does not recommend the use of stock images. However, if you are submitting a design that uses a stock image (ex: website design) it is mandatory to provide the source of the image. Please provide the source in the comment section when uploading. Logos and stationery should NEVER use stock and/or clipart images. Any draft not following these guidelines will be withdrawn. Thanks, QV/RTK Team

```html
<!DOCTYPE html>
<html lang="en">
<head>
<meta charset="utf-8">
<title>Hue Picker Bench – Tintmarble app</title>
<link rel="stylesheet" href="https://fonts.googleapis.com/css2?family=Arimo:wght@400;700&display=swap">
<style>
:root{
  --bar-blue:#3b5998;
  --ink:#111;
  --panel-dark:#16181d;
  --step-blue:#2d5fd8;
  --frame-grey:#d9d9d9;
  --photo-grey:#8e8e8e;
  --lite-blue:#1f6fd1;
  --full-red:#d8231c;
  --ad-blue:#1d5fa8;
  --ad-red:#c4161c;
  --ad-green:#5a9c1e;
  --text-grey:#555;
  --white:#fff;
}
*{box-sizing:border-box;margin:0;padding:0}
html,body{width:1200px;height:814px;overflow:hidden}
body{position:relative;background:var(--white);font-family:"Arimo",Arial,sans-serif;color:var(--ink)}
.abs{position:absolute}
.glow{position:absolute;border-radius:50%;filter:blur(30px)}
.glow-left{left:-120px;top:110px;width:560px;height:520px;background:radial-gradient(circle at 60% 50%,rgba(120,170,255,.45),rgba(255,120,200,.28) 45%,rgba(255,255,255,0) 70%)}
.glow-right{right:-120px;top:100px;width:560px;height:520px;background:radial-gradient(circle at 40% 45%,rgba(255,170,60,.45),rgba(240,80,200,.32) 40%,rgba(90,170,255,.25) 58%,rgba(255,255,255,0) 72%)}
.topbar{left:0;top:0;width:1200px;height:22px;background:var(--bar-blue)}
.topbar .brand{position:absolute;left:160px;top:3px;color:var(--white);font-weight:700;font-size:14px}
.topbar .search{position:absolute;left:288px;top:4px;width:216px;height:14px;background:var(--white);border:1px solid #24406f}
.likes{left:560px;top:29px;font-size:8px;color:var(--text-grey)}
.header{left:365px;top:48px;width:470px;height:58px;background:#000}
.header .logo{position:absolute;left:14px;top:19px;font-size:15px;font-weight:700;color:#e4388f;white-space:nowrap}
.header .tagline{position:absolute;left:205px;top:9px;font-size:13px;font-weight:700;color:var(--white);line-height:19px;white-space:nowrap}
.header .tagline em{font-style:normal;color:#ff4a4a}
.controls{left:365px;top:106px;width:72px;height:340px;background:var(--panel-dark)}
.step{width:64px;margin:4px auto 0;background:var(--step-blue);color:var(--white);font-size:9px;font-weight:700;text-align:center;padding:3px 0}
.btn-white{display:block;width:50px;margin:6px auto;background:var(--white);color:var(--step-blue);font-size:9px;font-weight:700;text-align:center;padding:6px 2px;border-radius:3px}
.controls .hint{color:#cfd6e6;font-size:7px;text-align:center;padding:4px 4px;line-height:9px}
.slider{position:relative;width:56px;height:3px;margin:8px auto;background:#8a8f9a}
.slider i{position:absolute;top:-5px;width:12px;height:12px;border-radius:50%;background:var(--white)}
.options{list-style:none;padding:4px 8px;color:#cfd6e6;font-size:7px;line-height:12px}
.options li::before{content:"";display:inline-block;width:6px;height:6px;border-radius:50%;border:1px solid #cfd6e6;margin-right:3px;vertical-align:-1px}
.stage{left:437px;top:106px;width:398px;height:340px;background:var(--frame-grey)}
.photo{position:absolute;left:24px;top:31px;width:353px;height:283px;background:linear-gradient(180deg,#9a9a9a,var(--photo-grey))}
.divider{left:365px;top:446px;width:470px;height:10px;background:#000}
.compare{left:365px;top:456px;width:470px;height:101px;background:var(--white);border:1px solid #ddd}
.compare .side{position:absolute;left:8px;top:6px;width:52px;height:88px;background:var(--lite-blue)}
.col{position:absolute;top:6px;width:160px}
.col h3{font-size:14px;font-weight:700}
.col h3 span{font-weight:400;color:var(--text-grey);font-size:11px}
.col ul{list-style:none;margin-top:4px;font-size:7px;color:var(--text-grey);line-height:12px}
.col li{white-space:nowrap}
.col li::before{content:"";display:inline-block;width:5px;height:5px;border-radius:50%;margin-right:4px}
.col-lite{left:72px}.col-lite h3{color:var(--lite-blue)}.col-lite li::before{background:var(--lite-blue)}
.col-full{left:242px}.col-full h3{color:var(--full-red)}.col-full li::before{background:var(--full-red)}
.col .deal{font-size:7px;color:var(--text-grey);margin-top:2px}
.col .deal b{color:var(--full-red)}
.compare .boxshot{position:absolute;right:10px;top:12px;width:48px;height:74px;background:linear-gradient(#2a2a30,#5a2a6a)}
.ads{left:367px;top:566px;width:463px;height:101px}
.ad{position:absolute;top:0;width:149px;height:101px;color:var(--white);padding:6px}
.ad h4{font-size:11px;font-weight:700}
.ad p{font-size:7px;line-height:9px;margin-top:3px;max-width:78px}
.ad-prints{left:0;background:linear-gradient(#2b78c8,var(--ad-blue))}
.ad-contest{left:156px;background:linear-gradient(#d9262b,var(--ad-red))}
.ad-offers{left:312px;background:linear-gradient(#78b82e,var(--ad-green))}
.ad .enter{position:absolute;left:22px;bottom:12px;background:var(--white);color:var(--ad-red);font-size:8px;font-weight:700;padding:3px 14px}
.ad .art{position:absolute;right:8px;top:26px;width:58px;height:56px;border-radius:3px}
.ad-prints .art{background:linear-gradient(#9cc6f0,#3d7fc2)}
.ad-contest .art{background:linear-gradient(#f2d6a8,#b8742c)}
.ad-offers .art{background:linear-gradient(#cfd8e4,#4a5870)}
.ad-offers .badge{position:absolute;left:10px;bottom:10px;width:30px;height:30px;border-radius:50%;background:var(--white)}
.shadow{left:380px;top:667px;width:440px;height:14px;background:radial-gradient(ellipse at 50% 0,rgba(0,0,0,.25),rgba(0,0,0,0) 70%)}
</style>
</head>
<body>
<div class="glow glow-left"></div>
<div class="glow glow-right"></div>

<header class="abs topbar">
  <span class="brand">Tintmarble</span>
  <span class="search"></span>
</header>
<div class="abs likes">Like · 1,024 people like this app</div>

<section class="abs header">
  <div class="logo">Hue Picker Bench V 2.0</div>
  <p class="tagline">Easily change your photos from <em>Color...</em><br>to Black &amp; White AND Color!</p>
</section>

<aside class="abs controls">
  <div class="step">STEP 1</div>
  <span class="btn-white">Open Photo</span>
  <div class="step">STEP 2</div>
  <p class="hint">Whatever you click the color will reappear</p>
  <div class="slider"><i style="left:34px"></i></div>
  <p class="hint">Cursor Size</p>
  <div class="slider"><i style="left:18px"></i></div>
  <ul class="options"><li>Add Color</li><li>Remove Color</li><li>Reset Colors</li></ul>
  <span class="btn-white" style="margin-top:14px">Save Photo</span>
</aside>

<section class="abs stage">
  <div class="photo" role="img" aria-label="Sample photo in the editing canvas: black and white close-up with one area kept in colour"></div>
</section>

<div class="abs divider"></div>

<section class="abs compare">
  <div class="side"></div>
  <div class="col col-lite">
    <h3>LITE <span>version</span></h3>
    <ul><li>Adjust colour areas with easy brushes</li><li>Works with most popular photo formats</li><li>Save edited photos straight to album</li></ul>
  </div>
  <div class="col col-full">
    <h3>FULL <span>version</span></h3>
    <ul><li>Unlimited layers and full size exports</li><li>Advanced edge detection for selections</li><li>Batch edit many photos in one go</li></ul>
    <p class="deal">click <b>HERE</b> to save <b>$10</b> off full version</p>
  </div>
  <div class="boxshot" role="img" aria-label="Product box of the full version"></div>
</section>

<section class="abs ads">
  <div class="ad ad-prints">
    <h4>PrintsOnSlate.example</h4>
    <p>Turn favorite photos into glass prints</p>
    <p>click HERE to save 20% on all products</p>
    <div class="art" role="img" aria-label="Framed photo print sample"></div>
  </div>
  <div class="ad ad-contest">
    <h4>PHOTO<br>CONTEST</h4>
    <p>Hue Picker Bench Lite</p>
    <span class="enter">ENTER</span>
    <div class="art" role="img" aria-label="Contest sample photo"></div>
  </div>
  <div class="ad ad-offers">
    <h4>BEST<br>OFFERS</h4>
    <p>Top picks for your desk</p>
    <span class="badge"></span>
    <div class="art" role="img" aria-label="Norvik laptop banner ad"></div>
  </div>
</section>
<div class="abs shadow"></div>
</body>
</html>
```